Modern Business Card

Modern professional business card with more than just logo and demographic info. Something memorable.

We are a trendy/modern chiropractic group with an emphasis on neurology, hence the minimalist-type brain logo. We want to convey that modern and technical aspect with professionalism and the elite nature of our practice environment.

```html
<!DOCTYPE html>
<html lang="en">
<head>
<meta charset="utf-8">
<title>Vantage Chiropractic – Business Card</title>
<link href="https://fonts.googleapis.com/css2?family=Lato:wght@400;700&family=Saira:wght@400;700&display=swap" rel="stylesheet">
<style>
  :root {
    --backdrop: #8c98a4;
    --card: #231f20;
    --card-edge: #6f6466;
    --silver: #e4dadb;
    --silver-mid: #b9a9ab;
    --silver-dim: #7d7173;
  }
  * { box-sizing: border-box; margin: 0; padding: 0; }
  html, body {
    width: 1049px; height: 1200px; overflow: hidden;
    background: var(--backdrop);
    font-family: "Lato", sans-serif;
  }
  .canvas { position: relative; width: 1049px; height: 1200px; }

  .card {
    position: absolute;
    left: 176px; width: 698px; height: 398px;
    background: var(--card);
    box-shadow: 0 0 0 1px var(--card-edge), 0 6px 14px rgba(0,0,0,.35);
    color: var(--silver);
  }
  .card--front { top: 159px; border-radius: 28px 0 28px 0; }
  .card--back  { top: 642px; border-radius: 0 28px 0 28px; }

  .brand {
    position: absolute; left: 0; right: 0;
    display: flex; align-items: center; justify-content: center;
    color: var(--silver-mid);
    font-family: "Lato", sans-serif; font-weight: 400;
    text-transform: uppercase; letter-spacing: .08em;
  }
  .brand__dot { border-radius: 50%; background: var(--silver-mid); flex: none; }
  .brand--small { top: 66px; font-size: 26px; gap: 14px; }
  .brand--small .brand__dot { width: 44px; height: 44px; }
  .brand--large { top: 150px; font-size: 46px; gap: 22px; }
  .brand--large .brand__dot { width: 90px; height: 90px; }

  .person {
    position: absolute; right: 367px; top: 180px;
    text-align: right; font-family: "Saira", sans-serif;
  }
  .person__name { font-size: 22px; font-weight: 700; color: var(--silver); line-height: 1.1; }
  .person__role { font-size: 14px; font-weight: 400; color: var(--silver-mid); letter-spacing: .02em; margin-top: 6px; }
  .person__rule { display: block; width: 36px; height: 2px; background: var(--silver-mid); margin: 8px 0 0 auto; }

  .divider {
    position: absolute; left: 351px; top: 186px;
    width: 3px; height: 56px; background: var(--silver-mid);
  }

  .contacts { position: absolute; left: 373px; top: 184px; list-style: none; }
  .contacts li {
    display: flex; align-items: center; gap: 9px;
    font-size: 16px; line-height: 20.5px; color: var(--silver);
  }
  .contacts svg { width: 12px; height: 12px; flex: none; }

  .address {
    position: absolute; left: 0; right: 0; top: 322px;
    text-align: center; font-size: 16px; color: var(--silver-mid); letter-spacing: .01em;
  }

  .web {
    position: absolute; left: 23px; top: 354px;
    display: flex; align-items: center; gap: 12px;
    font-size: 22px; color: var(--silver);
  }
  .web svg { width: 20px; height: 20px; }
  .icon { fill: none; stroke: var(--silver-mid); stroke-width: 1.4; }
</style>
</head>
<body>
<main class="canvas">

  <section class="card card--front" aria-label="Business card front">
    <div class="brand brand--small">
      <span class="brand__dot"></span>
      <span class="brand__name">Vantage Chiropractic</span>
    </div>

    <div class="person">
      <p class="person__name">DR. EVAN HOLLIS</p>
      <p class="person__role">CHIROPRACTIC</p>
      <span class="person__rule"></span>
    </div>

    <span class="divider"></span>

    <ul class="contacts">
      <li>
        <svg viewBox="0 0 12 12" class="icon"><rect x="3" y="0.8" width="6" height="10.4" rx="1"/><line x1="5.2" y1="9.4" x2="6.8" y2="9.4"/></svg>
        (555) 014- 2280
      </li>
      <li>
        <svg viewBox="0 0 12 12" class="icon"><rect x="0.8" y="2.5" width="10.4" height="7" /><polyline points="0.8,2.5 6,6.6 11.2,2.5"/></svg>
        evan@vantagechiro.com
      </li>
      <li>
        <svg viewBox="0 0 12 12" class="icon"><circle cx="6" cy="6" r="5.2"/><ellipse cx="6" cy="6" rx="2.3" ry="5.2"/><line x1="0.8" y1="6" x2="11.2" y2="6"/><line x1="1.6" y1="3.4" x2="10.4" y2="3.4"/><line x1="1.6" y1="8.6" x2="10.4" y2="8.6"/></svg>
        www.vantagechiro.com
      </li>
    </ul>

    <p class="address">1420 Maple Crest Ave, Springdale, OH 45001, United States</p>
  </section>

  <section class="card card--back" aria-label="Business card back">
    <div class="brand brand--large">
      <span class="brand__dot"></span>
      <span class="brand__name">Vantage Chiropractic</span>
    </div>

    <p class="web">
      <svg viewBox="0 0 12 12" class="icon"><circle cx="6" cy="6" r="5.2"/><ellipse cx="6" cy="6" rx="2.3" ry="5.2"/><line x1="0.8" y1="6" x2="11.2" y2="6"/><line x1="1.6" y1="3.4" x2="10.4" y2="3.4"/><line x1="1.6" y1="8.6" x2="10.4" y2="8.6"/></svg>
      www.vantagechiro.com
    </p>
  </section>

</main>
</body>
</html>
```